Velter Labs - Mushroom Supplement Packaging

Our brand is called Velter Labs. I've added a couple different logos that you can use. We are creating a line up of Mushroom Supplement products. I will add the entire line-up of products here. I've added examples of other products and packaging shape types I can purchase. Give me different options for packaging that is minimalist and clean for this brand that makes it look really well made and clean and make people want to buy.

Product 1 Lions Mane 1g
Product 2 Cordyceps 1g
Product 3 Chaga 1g
Product 4 Turkey Tail 1g
Product 5 Reishi 1g
Product 6 Maitake 1g
Product 7 Shiitake 1g

Product 8 (Mix) Lions Mane 143mg
Cordyceps 143mg
Chaga 143mg
Turkey Tail 143mg
Reishi 143mg
Maitake 143mg
Shiitake 143mg

```html
<!DOCTYPE html>
<html lang="en">
<head>
<meta charset="UTF-8">
<title>Velter Labs – Lion's Mane Label</title>
<link rel="stylesheet" href="https://fonts.googleapis.com/css2?family=Oswald:wght@500;600;700&family=Montserrat:wght@600;700&display=swap">
<style>
  :root {
    --teal: #6dbfc4;
    --teal-deep: #56b1b6;
    --label-light: #ececed;
    --label-mid: #dcdcde;
    --ink-gray: #5a5b5e;
    --ink-dark: #161616;
    --ink-body: #3c3d40;
    --white: #ffffff;
    --page: #f7f7f7;
  }
  * { margin: 0; padding: 0; box-sizing: border-box; }
  html, body {
    width: 1200px; height: 1200px; overflow: hidden;
    background: var(--page);
  }
  .label {
    position: absolute;
    left: 130px; top: 42px;
    width: 940px; height: 1115px;
    background: linear-gradient(90deg, var(--label-mid) 0%, var(--label-light) 30%, var(--label-light) 70%, var(--label-mid) 100%);
    overflow: hidden;
  }
  .brand-band {
    position: absolute; left: 0; top: 0;
    width: 100%; height: 302px;
    background: var(--teal);
    display: flex; align-items: center; justify-content: center;
  }
  .brand-name {
    font-family: "Oswald", sans-serif;
    font-weight: 600;
    font-size: 78px;
    letter-spacing: 2px;
    color: var(--white);
    text-transform: uppercase;
  }
  .product-name {
    position: absolute; left: 0; top: 405px; width: 100%;
    text-align: center;
    font-family: "Oswald", sans-serif;
    font-weight: 700;
    font-size: 150px;
    line-height: 1;
    letter-spacing: 4px;
  }
  .product-name .word-lead { color: var(--ink-gray); }
  .product-name .word-tail { color: var(--ink-dark); }
  .benefit-pill {
    position: absolute; left: 181px; top: 635px;
    width: 578px; height: 87px;
    background: var(--teal-deep);
    border-radius: 10px;
    display: flex; align-items: center; justify-content: center;
    font-family: "Oswald", sans-serif;
    font-weight: 500;
    font-size: 50px;
    letter-spacing: 1px;
    color: var(--white);
  }
  .benefit-list {
    position: absolute; left: 181px; top: 806px;
    list-style: none;
    font-family: "Montserrat", sans-serif;
    font-weight: 600;
    font-size: 29px;
    color: var(--ink-body);
  }
  .benefit-list li {
    display: flex; align-items: center; gap: 14px;
    height: 42px;
  }
  .benefit-list svg { width: 20px; height: 20px; flex: none; }
  .count-tag {
    position: absolute; left: 215px; top: 987px;
    height: 42px; padding: 0 6px;
    background: var(--teal-deep);
    border-radius: 5px;
    font-family: "Montserrat", sans-serif;
    font-weight: 700;
    font-size: 33px;
    line-height: 42px;
    color: var(--white);
  }
  .supplement-note {
    position: absolute; left: 215px; top: 1062px;
    font-family: "Montserrat", sans-serif;
    font-weight: 700;
    font-size: 28px;
    color: var(--ink-body);
  }
</style>
</head>
<body>
  <main class="label">
    <header class="brand-band">
      <span class="brand-name">Velter Labs</span>
    </header>

    <h1 class="product-name"><span class="word-lead">LION'S</span> <span class="word-tail">MANE</span></h1>

    <div class="benefit-pill">FOCUS - CLARITY - MOOD</div>

    <ul class="benefit-list">
      <li><svg viewBox="0 0 20 20"><path d="M3 11 L8 16 L17 4" fill="none" stroke="#56b1b6" stroke-width="2.6" stroke-linecap="round" stroke-linejoin="round"/></svg>Improved Focus, Memory &amp; Mood</li>
      <li><svg viewBox="0 0 20 20"><path d="M3 11 L8 16 L17 4" fill="none" stroke="#56b1b6" stroke-width="2.6" stroke-linecap="round" stroke-linejoin="round"/></svg>Stress &amp; Anxiety Reduction</li>
      <li><svg viewBox="0 0 20 20"><path d="M3 11 L8 16 L17 4" fill="none" stroke="#56b1b6" stroke-width="2.6" stroke-linecap="round" stroke-linejoin="round"/></svg>Immune System Support</li>
    </ul>

    <div class="count-tag">60 CAPSULES</div>
    <p class="supplement-note">DIETARY SUPPLEMENT</p>
  </main>
</body>
</html>
```